International Manufacturing Business Needs A Heavy Hitting Wordpress Design!

We need wordpress template designs for a new website for our UK based International company Tolvane Engineering Ltd. We manufacture and supply steel security doors and window units. We would like designs that feature the black and yellow industrial "stripes" that can be seen at our current site www.tolvadoors.com. The final design should communicate strength, power and weight to represent the quality of the products and the security that they provide.

It feels like we need 3 different types of page to be able to be created as per the current website at www.tolvasecuredoors.com.

Homepage
Products/Accessories
Leadtimes/Downloads/Contact

It may be that 3 different page types can be created with one template. I'm totally open to this.

I don't like the way that the site currently handles product images, nobody wants to click on even thumbnail to see the product. http://tolvasecuredoors.com/products/personnel-doors/

Totally open to suggestions on layout to enable the feeling outlined in the brief above.

Please ask if anything is not clear or you need answers to drill down on specifics.

Sick

Target Market(s)

Businesses that buy steel doors

Font styles to use
Sans Serif
Other font styles liked:
• Copperplate Gothic Bold - For Company Name but we are open to suggestions

Colors

Designer to choose colors to be used in the design.

Requirements
Must have
• Professional looking, clean design
• Conveys strength, power and weight to represent the quality of the products, the characteristics of steel and the security that they provide.
• Incorporates black and yellow stripes of our branding
• Ability to create pages with content as seen at www.tolvasecuredoors.com
• A better way of showing the product images
Nice to have
• If possible. a design that gives off the feeling that not only do we supply the products we also make them in house too. I don't know what this looks like but a way of differentiating between a supply only business and one that manufacturers the product too.
Should not have
• We don't like the current thumbnail method of showing the product images

```html
<!DOCTYPE html>
<html lang="en">
<head>
<meta charset="utf-8">
<title>Tolvane Engineering Ltd — Security Doors</title>
<link rel="stylesheet" href="https://fonts.googleapis.com/css2?family=Montserrat:wght@400;500;600;700&family=Roboto+Slab:wght@400;600;700&display=swap">
<style>
:root{
  --ink:#0b0c05;
  --yellow:#f7d22a;
  --green:#5a9e73;
  --white:#ffffff;
  --nav:#77776f;
  --muted:#a9a795;
  --dark:#242422;
  --title-grey:#c4c2b8;
}
*{margin:0;padding:0;box-sizing:border-box}
html,body{width:1200px;height:1200px;overflow:hidden;background:var(--ink)}
body{font-family:'Montserrat',sans-serif;position:relative}
.slab{font-family:'Roboto Slab',serif}

.topbar{position:absolute;left:0;top:0;width:1200px;height:29px;background:var(--ink);
  font-size:13px;font-weight:600;color:var(--white);display:flex;align-items:center}
.topbar .phone{position:absolute;left:99px}
.topbar .email{position:absolute;left:245px;color:var(--yellow)}
.topbar .social{position:absolute;right:98px;display:flex;gap:14px;font-size:11px;color:var(--yellow)}

.header{position:absolute;left:0;top:29px;width:1200px;height:123px;background:var(--white)}
.brand{position:absolute;left:98px;top:40px;display:flex;align-items:center;gap:12px}
.brand .mark{width:50px;height:50px;background:var(--green)}
.brand .name{font-family:'Roboto Slab',serif;font-weight:700;color:var(--ink);line-height:1.05;font-size:24px}
.brand .name span{display:block;font-size:15px}
.nav{position:absolute;right:96px;top:56px;display:flex;gap:20px;list-style:none;
  font-family:'Roboto Slab',serif;font-weight:600;font-size:12px;color:var(--nav);letter-spacing:.2px}

.hazard{position:absolute;left:0;top:152px;width:1200px;height:10px;background:var(--white)}
.hazard svg{display:block}

.hero{position:absolute;left:0;top:162px;width:1200px;height:470px;background:var(--ink)}
.hero-photo{position:absolute;left:608px;top:0;width:552px;height:470px;
  background:linear-gradient(90deg,#0d0e08 0%,#1c1a10 30%,#6d6a63 52%,#8a7a20 70%,#e7c21c 85%,#3a3510 100%)}
.hero-kicker{position:absolute;left:94px;top:110px;font-family:'Roboto Slab',serif;font-size:35px;
  color:var(--muted);letter-spacing:.5px}
.hero-title{position:absolute;left:94px;top:162px;font-weight:700;font-size:52px;line-height:52px;color:var(--white)}
.btn{position:absolute;top:312px;width:208px;height:48px;display:flex;align-items:center;justify-content:center;
  font-family:'Roboto Slab',serif;font-weight:700;font-size:17px}
.btn-products{left:100px;background:var(--yellow);color:var(--ink)}
.btn-about{left:324px;background:var(--green);color:var(--white)}

.intro{position:absolute;left:0;top:632px;width:1200px;height:225px}
.intro svg{position:absolute;left:0;top:0}
.intro h2{position:absolute;left:0;width:1200px;top:90px;text-align:center;font-family:'Roboto Slab',serif;
  font-weight:700;font-size:28px;color:var(--white);letter-spacing:.5px}
.intro p{position:absolute;left:0;width:1200px;top:130px;text-align:center;font-weight:600;font-size:17px;color:#2b2708}

.about{position:absolute;left:0;top:835px;width:1200px;height:365px;z-index:-0}
.about-bg{position:absolute;inset:0;background:radial-gradient(ellipse at 50% 40%,#3a3935 0%,#262523 55%,#1a1a18 100%)}
.about .col{position:absolute;top:80px;width:505px;font-size:14px;line-height:22px;color:var(--white)}
.about .col p{margin-bottom:9px}
.about .left{left:70px}
.about .right{left:617px}
.divider{position:absolute;left:548px}
.featured{position:absolute;left:0;width:1200px;top:315px;text-align:center;font-family:'Roboto Slab',serif;
  font-weight:700;font-size:28px;color:var(--title-grey)}
.intro{z-index:2}
</style>
</head>
<body>

<div class="topbar">
  <span class="phone">+44 (0)1632 960 418</span>
  <span class="email">sales@tolvadoors.com</span>
  <span class="social"><span>Follow</span><span>Connect</span></span>
</div>

<header class="header">
  <div class="brand">
    <div class="mark"></div>
    <div class="name">TOLVANE<span>ENGINEERING LTD.</span></div>
  </div>
  <ul class="nav">
    <li>HOME</li><li>PRODUCTS</li><li>ACCESSORIES</li><li>DELIVERY &amp; LEAD TIMES</li>
    <li>DOWNLOADS</li><li>ORDER FORM</li><li>CONTACT</li>
  </ul>
</header>

<div class="hazard">
  <svg width="1200" height="10" viewBox="0 0 1200 10">
    <defs>
      <pattern id="hazard-dash" width="40" height="10" patternUnits="userSpaceOnUse">
        <polygon points="12,0 34,0 30,7 8,7" fill="#f7d22a"/>
      </pattern>
    </defs>
    <rect width="1200" height="10" fill="url(#hazard-dash)"/>
  </svg>
</div>

<section class="hero">
  <div class="hero-photo" role="img" aria-label="Close-up of a panic bar push handle on a yellow steel security door"></div>
  <div class="hero-kicker">TOLVANE ENGINEERING</div>
  <h1 class="hero-title">Manufacturers &amp; Suppliers<br>of Security Doors</h1>
  <div class="btn btn-products">VIEW PRODUCTS</div>
  <div class="btn btn-about">MORE ABOUT US</div>
</section>

<section class="intro">
  <svg width="1200" height="225" viewBox="0 0 1200 225">
    <polygon points="0,0 1200,0 1200,203 600,223 0,203" fill="#f7d22a"/>
    <polygon points="553,65 573,65 569,72 549,72" fill="#2b2708"/>
    <polygon points="593,65 613,65 609,72 589,72" fill="#2b2708"/>
    <polygon points="633,65 653,65 649,72 629,72" fill="#2b2708"/>
  </svg>
  <h2>SUPERIOR QUALITY &amp; PROVEN RELIABILITY</h2>
  <p>Tolvane security doors combine a high level of security with exceptional value …</p>
</section>

<section class="about">
  <div class="about-bg" role="img" aria-label="Blurred view of the steel door manufacturing workshop"></div>
  <div class="col left">
    <p>Our superior quality and proven reliability has made us the first choice for a wide range of companies no matter what their requirement or application.</p>
    <p>All of our products are designed and manufactured to the highest specification, combine this with a rigorous quality control system and an extensive after-sales service and it is easy to see why we are seen as industry leaders.</p>
  </div>
  <div class="col right">
    <p>We place particular emphasis on continuous development and twelve years experience ensures that we are always ahead of the competition and that we can react quickly to customer’s requirements.</p>
    <p>Each and every Tolvane product is subject to our fifty point quality control process before it is dispatched.</p>
    <p>Tolvane have forged a reputation for affordable, high quality steel doors.</p>
  </div>
  <svg class="divider" width="104" height="8" viewBox="0 0 104 8" style="top:274px">
    <polygon points="4,0 24,0 20,7 0,7" fill="#f7d22a"/>
    <polygon points="44,0 64,0 60,7 40,7" fill="#f7d22a"/>
    <polygon points="84,0 104,0 100,7 80,7" fill="#f7d22a"/>
  </svg>
  <h2 class="featured">FEATURED PRODUCTS</h2>
</section>

</body>
</html>
```